KOR Methodology infographic that shows flow of the process outlined on our web site

We are looking for a graphical representation of the methodology that is described on this web page: https://www.kor-example.com/about-kor/methodology/ We would like someone to be able to quickly understand our methodology and the key points outlined on the web page - the graphic should be able to do that.

Target Market(s)

Enterprise Companies with 1000+ employees

Industry/Entity Type

Information Technology

Font styles to use
Sans Serif

Colors
3277b5
abd036
faa54b

Requirements
Must have
• Must convey the method/process with enough detail to understand what the process is.
Nice to have
• Arrows or something showing flow would be great
Should not have
• Should not be "cartoony"

```html
<!DOCTYPE html>
<html lang="en">
<head>
<meta charset="utf-8">
<title>KOR Methodology</title>
<link rel="stylesheet" href="https://fonts.googleapis.com/css2?family=Arimo:wght@400;700&display=swap">
<style>
  :root {
    --blue: #3277b5;
    --green: #abd036;
    --orange: #faa54b;
    --text: #555a5e;
    --card-light: #f7f8f9;
    --card-dark: #cfd3d7;
    --frame: #c9c9c9;
    --bg: #ffffff;
  }
  * { box-sizing: border-box; margin: 0; padding: 0; }
  html, body { width: 1200px; height: 900px; overflow: hidden; background: var(--bg); }
  .methodology {
    position: relative;
    width: 1200px;
    height: 900px;
    border: 1px solid var(--frame);
    font-family: "Arimo", Arial, sans-serif;
    background: var(--bg);
  }
  .flow { position: absolute; left: 0; top: 0; }
  .step-card {
    position: absolute;
    width: 445px;
    height: 232px;
    border: 1px solid #b9bdc1;
    border-radius: 4px;
    background: linear-gradient(135deg, var(--card-dark) 0%, var(--card-light) 45%, var(--card-light) 60%, var(--card-dark) 100%);
    box-shadow: 2px 2px 4px rgba(0,0,0,0.12);
    padding: 12px 12px 0 12px;
  }
  .step-card h2 {
    font-weight: 400;
    font-size: 33px;
    color: var(--blue);
    text-align: center;
    line-height: 42px;
    margin-bottom: 4px;
  }
  .step-card p {
    font-size: 15.5px;
    line-height: 22px;
    color: var(--text);
    text-align: justify;
  }
  .step-card--consultation { left: 108px; top: 78px; }
  .step-card--development { left: 650px; top: 78px; }
  .step-card--assessment { left: 108px; top: 628px; padding-top: 20px; }
  .step-card--implementation { left: 650px; top: 628px; padding-top: 14px; }
  .step-card--assessment h2, .step-card--implementation h2 { margin-bottom: 18px; }
</style>
</head>
<body>
<main class="methodology">
  <svg class="flow" width="1200" height="900" viewBox="0 0 1200 900" aria-hidden="true">
    <defs>
      <linearGradient id="badge-fill" x1="0" y1="0" x2="1" y2="1">
        <stop offset="0" stop-color="#ffffff"/>
        <stop offset="0.55" stop-color="#eceef0"/>
        <stop offset="1" stop-color="#c7cbcf"/>
      </linearGradient>
    </defs>

    <!-- process path -->
    <path d="M191 470 A99 99 0 0 0 389 470 A99 99 0 0 1 587 470 A99 99 0 0 0 785 470 A99 99 0 0 1 983 470 L1000 470"
          fill="none" stroke="var(--orange)" stroke-width="28"/>

    <!-- flow arrows -->
    <g fill="var(--blue)">
      <polygon points="174,400 206,400 190,416"/>
      <polygon points="174,422 206,422 190,438"/>
      <polygon points="174,444 206,444 190,460"/>
      <polygon points="971,477 1003,477 987,493"/>
      <polygon points="971,499 1003,499 987,515"/>
      <polygon points="971,521 1003,521 987,537"/>
    </g>

    <!-- connectors -->
    <g stroke="var(--green)" stroke-width="4" fill="var(--green)">
      <line x1="290" y1="318" x2="290" y2="374"/><circle cx="290" cy="318" r="8" stroke="none"/><circle cx="290" cy="374" r="8" stroke="none"/>
      <line x1="690" y1="318" x2="690" y2="374"/><circle cx="690" cy="318" r="8" stroke="none"/><circle cx="690" cy="374" r="8" stroke="none"/>
      <line x1="488" y1="562" x2="488" y2="617"/><circle cx="488" cy="562" r="8" stroke="none"/><circle cx="488" cy="617" r="8" stroke="none"/>
      <line x1="886" y1="562" x2="886" y2="617"/><circle cx="886" cy="562" r="8" stroke="none"/><circle cx="886" cy="617" r="8" stroke="none"/>
    </g>

    <!-- step badges -->
    <g stroke="#c4c7ca" stroke-width="1.5" fill="url(#badge-fill)">
      <circle cx="290" cy="468" r="82"/>
      <circle cx="488" cy="468" r="82"/>
      <circle cx="688" cy="468" r="82"/>
      <circle cx="886" cy="468" r="82"/>
    </g>

    <!-- headset icon -->
    <g fill="none" stroke="var(--blue)" stroke-width="7" stroke-linecap="round">
      <path d="M258 468 A32 32 0 0 1 322 468"/>
      <path d="M318 488 Q316 508 292 510"/>
    </g>
    <g fill="var(--blue)">
      <rect x="250" y="460" width="16" height="30" rx="6"/>
      <rect x="314" y="460" width="16" height="30" rx="6"/>
      <circle cx="290" cy="510" r="6"/>
    </g>

    <!-- checklist icon -->
    <g>
      <rect x="452" y="425" width="68" height="86" rx="5" fill="var(--blue)"/>
      <rect x="472" y="416" width="28" height="16" rx="4" fill="var(--blue)" stroke="#fff" stroke-width="3"/>
      <g stroke="#fff" stroke-width="3" fill="none">
        <polyline points="461,446 465,450 471,442"/><line x1="477" y1="447" x2="510" y2="447"/>
        <polyline points="461,462 465,466 471,458"/><line x1="477" y1="463" x2="510" y2="463"/>
        <polyline points="461,478 465,482 471,474"/><line x1="477" y1="479" x2="500" y2="479"/>
        <polyline points="461,494 465,498 471,490"/><line x1="477" y1="495" x2="494" y2="495"/>
      </g>
      <circle cx="518" cy="503" r="20" fill="var(--blue)" stroke="#fff" stroke-width="3"/>
      <polyline points="508,503 515,510 528,496" fill="none" stroke="#fff" stroke-width="4"/>
    </g>

    <!-- code window icon -->
    <g>
      <rect x="646" y="422" width="88" height="86" rx="3" fill="var(--blue)"/>
      <rect x="652" y="436" width="76" height="66" fill="none"/>
      <line x1="646" y1="438" x2="734" y2="438" stroke="#fff" stroke-width="2"/>
      <g fill="#fff"><circle cx="655" cy="430" r="2.5"/><circle cx="663" cy="430" r="2.5"/><circle cx="671" cy="430" r="2.5"/><rect x="678" y="428" width="50" height="4"/></g>
      <g fill="none" stroke="#fff" stroke-width="4" stroke-linecap="round">
        <polyline points="672,462 662,472 672,482"/>
        <polyline points="708,462 718,472 708,482"/>
        <line x1="695" y1="458" x2="685" y2="486"/>
      </g>
    </g>

    <!-- gears icon -->
    <g fill="var(--blue)">
      <circle cx="860" cy="442" r="16"/>
      <g transform="translate(860 442)">
        <rect x="-5" y="-24" width="10" height="48"/>
        <rect x="-5" y="-24" width="10" height="48" transform="rotate(45)"/>
        <rect x="-5" y="-24" width="10" height="48" transform="rotate(90)"/>
        <rect x="-5" y="-24" width="10" height="48" transform="rotate(135)"/>
      </g>
      <circle cx="905" cy="485" r="26"/>
      <g transform="translate(905 485)">
        <rect x="-6" y="-36" width="12" height="72"/>
        <rect x="-6" y="-36" width="12" height="72" transform="rotate(45)"/>
        <rect x="-6" y="-36" width="12" height="72" transform="rotate(90)"/>
        <rect x="-6" y="-36" width="12" height="72" transform="rotate(135)"/>
      </g>
      <circle cx="860" cy="442" r="7" fill="#f1f2f3"/>
      <circle cx="905" cy="485" r="12" fill="#f1f2f3"/>
      <polygon points="894,474 914,478 898,494" fill="var(--blue)"/>
    </g>
  </svg>

  <section class="step-card step-card--consultation">
    <h2>Initial Consultation</h2>
    <p>A first conversation in any relationship is vitally important. This is especially true when beginning an IT project. Setting expectations and defining success are integral parts of the process. An initial consultation with KOR will be filled with questions and listening as we discover the concerns you have and consider the best approach to help you achieve your goals.</p>
  </section>

  <section class="step-card step-card--development">
    <h2>Solution Development</h2>
    <p>Your KOR team includes members of the account management, engineering, and finance departments. After initial consultations and assessments are completed, your team convenes to design and draw up solutions for your consideration.</p>
  </section>

  <section class="step-card step-card--assessment">
    <h2>Assessment</h2>
    <p>Very often after an initial consultation is over, the process is best served by adding an assessment phase. This process can range from simple interviews to full enterprise evaluations. The assessment stage should end with the discovery of all pertinent information needed for the development of an effective solution.</p>
  </section>

  <section class="step-card step-card--implementation">
    <h2>Implementation</h2>
    <p>Upon acceptance of a quote and a subsequent purchase order, the certified KOR engineers proceed with your implementation.</p>
  </section>
</main>
</body>
</html>
```